Guaranteed Job - Sleek Sexy Business Card UV Spot

Im looking for a sleek and sexy business card, that resembles elite or VIP status status.
our business is corinvale.example
you can view our products on there, but our main audience for handing out our cards will be for people in the hospitality industry, so it will need to impress high management and CEO of hotels and restaurants, bars, clubs etc...
the card features will have UV spot on both sides, 400gsm stock. standard size.
Artwork should be 86 x 54mm + 2mm bleed = 90 x 58mm
it should have a nice "unique" uv spot pattern that highlights the card, not a repeated pattern, theres no originality there, and it will be disregarded.
The written material will be:
Corin Vale Hospitality College (logo)
Tobin Marsh
Director
Phone: 1300 615 737
Mobile: 0455 817 296
Email: info@corinvale.example
website: www.corinvale.example
I'm looking for originality here, i don't want just a simple stock card, want something that has a wow factor for people.
You will find the logo attached. you may invert the white to black words to suit the background as you please.
thank you and good luck
As a side note, ive received a lot of proposals, im too busy to give feedback to each and every one, so if i havent provided feedback for your design within 24 hours, then consider it not acceptable, and you could resubmit another design.
So far i have not seen any design that stood out for me, they all seem pretty generic. there nothing thats unique, i would figure for the amount that im offering, that people would put some more effort and creativity into the design.
so far over 200 designs submitted, and nothing i have seen looks very original, everything looks like a different variation of the same stuff, i said it very clearly i wanted something unique, the only thing that has come close to it so far is this one
Reason: Ive received alot of design concepts and i have reviewed everyone, but i havent had time to give feedback to every single one, only the ones that have interested me, if i havent responded, its because i havent found it good enough.
so far only a few design have been on par with what ive been looking for, an attractive eye popping design.
heres a few of them,
http://files.pixelbazaar.example/design_img/51736/62418/62418_2840915_51736_image.jpg
http://files.pixelbazaar.example/design_img/51736/68254/68254_2841377_51736_image.jpg
theyre, both unique and original, and eye catching, the only thing theyre missing is the sexyness.
if you still think you have some creativity left in your minds, then throw it on here.
Reason: Sorry guys for the delay, I was in a serious accident and out of commission for the past few months, I'm just slowly recovering now, please bare with me as i try to attend to this project, it may take me awhile as I have other projects that are on standby, I'm not 100% at the moment, so im extending the deadline for 2 weeks right now. Thanks for your patience.
Hospitality

```html
<!DOCTYPE html>
<html lang="en">
<head>
<meta charset="utf-8">
<title>Corin Vale Hospitality College – Business Card</title>
<link rel="stylesheet" href="https://fonts.googleapis.com/css2?family=PT+Sans:ital,wght@0,400;0,700;1,700&family=Questrial&display=swap">
<style>
  :root {
    --page-bg: #e9e8e5;
    --card-dark: #1f2328;
    --card-dark-edge: #15181c;
    --pattern-tone: #2c3440;
    --band-blue: #5b9ac7;
    --band-blue-deep: #4a86b3;
    --band-blue-light: #6aa8d3;
    --icon-navy: #1d3550;
    --text-white: #ffffff;
    --accent-blue: #4fa8e0;
    --sans: "PT Sans", sans-serif;
    --contact: "Questrial", sans-serif;
  }
  * { box-sizing: border-box; margin: 0; padding: 0; }
  html, body {
    width: 1200px; height: 911px; overflow: hidden;
    background: var(--page-bg);
  }
  .canvas { position: relative; width: 1200px; height: 911px; }

  .card {
    position: absolute; top: 321px;
    width: 552px; height: 357px;
    background: var(--card-dark); overflow: hidden;
  }
  .card--front { left: 26px; }
  .card--back { left: 616px; }

  .card__pattern {
    position: absolute; inset: 0;
    background:
      radial-gradient(circle at 50% 50%, var(--pattern-tone) 0%, var(--card-dark) 70%, var(--card-dark-edge) 100%);
  }
  .card__band {
    position: absolute; left: 0; right: 0; top: 141px; height: 87px;
    background: linear-gradient(180deg, var(--band-blue-light), var(--band-blue) 50%, var(--band-blue-deep));
    box-shadow: 0 0 8px rgba(0,0,0,.6);
  }

  .brand {
    position: absolute; left: 194px; top: 62px;
    display: flex; align-items: center; gap: 10px;
    color: var(--text-white);
    font-family: var(--sans); font-weight: 700;
  }
  .brand__mark { width: 14px; height: 14px; background: var(--text-white); }
  .brand__name {
    font-size: 16px; line-height: 1.15; text-transform: uppercase; letter-spacing: .5px;
    width: 170px;
  }

  .contact {
    position: absolute; display: flex; align-items: center; gap: 12px;
    font-family: var(--contact); color: var(--text-white);
  }
  .contact svg { width: 24px; height: 24px; flex: none; }
  .contact--phone { left: 56px; top: 146px; font-size: 20px; letter-spacing: 1px; }
  .contact--mobile { left: 56px; top: 184px; font-size: 20px; letter-spacing: 1px; }
  .contact--email { left: 282px; top: 148px; font-size: 14.5px; letter-spacing: .8px; }
  .contact--web { left: 282px; top: 186px; font-size: 14.5px; letter-spacing: .8px; }

  .person {
    position: absolute; left: 196px; top: 236px;
    font-family: var(--sans); color: var(--text-white);
  }
  .person__name { font-size: 34px; font-weight: 700; letter-spacing: -.3px; }
  .person__role {
    margin-left: 34px; margin-top: -4px;
    font-size: 16px; font-weight: 700; font-style: italic; color: var(--accent-blue);
  }
</style>
</head>
<body>
<main class="canvas">

  <section class="card card--front" aria-label="Business card front">
    <div class="card__pattern" role="img" aria-label="Dark damask ornament pattern with spot UV finish"></div>
    <div class="card__band" role="img" aria-label="Blue band with subtle damask ornament pattern"></div>

    <div class="brand">
      <span class="brand__mark"></span>
      <span class="brand__name">Corin Vale Hospitality College</span>
    </div>

    <div class="contact contact--phone">
      <svg viewBox="0 0 24 24" aria-hidden="true"><circle cx="12" cy="12" r="11" fill="var(--icon-navy)"/><path d="M8 6.5c.6-.4 1.3-.3 1.6.3l1 1.8c.3.5.1 1.1-.3 1.4l-.7.5c.6 1.4 1.6 2.5 3 3.2l.6-.7c.4-.4 1-.5 1.4-.2l1.8 1.1c.5.3.7 1 .3 1.5-.8 1.1-2 1.6-3.2 1.1-3-1.2-5.3-3.6-6.3-6.6-.4-1.2.1-2.4.8-2.9z" fill="var(--band-blue-light)"/></svg>
      <span>1300 615 737</span>
    </div>
    <div class="contact contact--mobile">
      <svg viewBox="0 0 24 24" aria-hidden="true"><rect x="6" y="1.5" width="12" height="21" rx="2.5" fill="var(--icon-navy)"/><rect x="8" y="4.5" width="8" height="12" fill="var(--band-blue-light)"/><circle cx="12" cy="19.3" r="1.2" fill="var(--band-blue-light)"/></svg>
      <span>0455 817 296</span>
    </div>
    <div class="contact contact--email">
      <svg viewBox="0 0 24 24" aria-hidden="true"><rect x="2" y="5" width="20" height="14" rx="1.5" fill="var(--icon-navy)"/><path d="M3 6.5l9 6.5 9-6.5" fill="none" stroke="var(--band-blue-light)" stroke-width="1.5"/></svg>
      <span>info@corinvale.example</span>
    </div>
    <div class="contact contact--web">
      <svg viewBox="0 0 24 24" aria-hidden="true"><circle cx="12" cy="12" r="10" fill="var(--icon-navy)"/><g fill="none" stroke="var(--band-blue-light)" stroke-width="1.2"><ellipse cx="12" cy="12" rx="4.5" ry="10"/><path d="M2 12h20M4 7h16M4 17h16"/></g></svg>
      <span>www.corinvale.example</span>
    </div>

    <div class="person">
      <p class="person__name">Tobin Marsh</p>
      <p class="person__role">Director</p>
    </div>
  </section>

  <section class="card card--back" aria-label="Business card back">
    <div class="card__pattern" role="img" aria-label="Dark damask ornament pattern with spot UV finish"></div>
    <div class="card__band" role="img" aria-label="Blue band with subtle damask ornament pattern"></div>
  </section>

</main>
</body>
</html>
```